Make a medical leaflet for my patients undergoing ankle blocks

I have a very boring text only leaflet I would like to turn into a professional appealing medical leaflet to give to my patients. I would like to get this onto two pages of a4 if possible and its intended for electronic distribution mainly.
This will be for patients so it must be professional.
It must also contain a copyright logo on it and my name near the start (Dr Tobias Wendell) so my colleagues can't use it easily.
Target Market(s)
Patients undergoing surgery
Industry/Entity Type
Medical
Font styles to use
Other font styles liked:
- no idea, you tell me
Requirements
Must have
- the information contained on the attachment
- look professional
- a copyright on it
Nice to have
- the ashbury clinic logo
Should not have
- Any spelling, grammatical or linguistic errors
- Any font less than size 12

```html
<!DOCTYPE html>
<html lang="en">
<head>
<meta charset="utf-8">
<title>Ankle Block – Patient Information</title>
<link href="https://fonts.googleapis.com/css2?family=Open+Sans:ital,wght@0,400;0,600;0,700;1,700;1,800&display=swap" rel="stylesheet">
<style>
  :root {
    --backdrop: #dfe4e6;
    --paper: #ffffff;
    --ink: #3c4650;
    --muted: #6a7580;
    --navy: #1b3a8c;
    --brand-blue: #2d6fe0;
    --cyan: #3fd8f5;
    --sky: #5fb0ff;
    --pale: #e6f8fd;
  }
  * { box-sizing: border-box; margin: 0; padding: 0; }
  html, body {
    width: 1200px; height: 1063px; overflow: hidden;
    background: var(--backdrop);
    font-family: "Open Sans", Arial, sans-serif;
    color: var(--ink);
  }
  .spread { position: relative; width: 1200px; height: 1063px; }
  .page {
    position: absolute; top: 30px;
    width: 582px; height: 1000px;
    background: var(--paper);
    box-shadow: 0 10px 28px rgba(40, 60, 70, 0.22);
    overflow: hidden;
  }
  .page--front { left: 12px; }
  .page--back { left: 606px; }
  .wave { position: absolute; left: 0; width: 100%; display: block; }
  .wave--top { top: 0; height: 70px; }
  .wave--bottom { bottom: 0; height: 62px; }
  .page__body {
    position: relative;
    padding: 0 28px;
    font-size: 11px;
    line-height: 1.38;
  }
  .page--front .page__body { padding-top: 62px; }
  .page--back .page__body { padding-top: 66px; }

  .masthead { display: flex; justify-content: space-between; align-items: flex-start; }
  .title {
    font-weight: 800; font-style: italic;
    font-size: 32px; color: var(--navy); line-height: 1.1;
  }
  .title::after {
    content: ""; display: block;
    width: 24px; height: 3px; margin-top: 6px;
    background: var(--navy);
  }
  .clinic-name {
    display: flex; align-items: center; gap: 8px;
    margin-top: 6px;
    font-size: 14px; font-weight: 600; letter-spacing: 0.12em;
    text-transform: uppercase; color: var(--brand-blue);
  }
  .clinic-name__mark { width: 12px; height: 12px; background: var(--brand-blue); }
  .author {
    font-size: 12px; font-weight: 600; color: var(--navy);
    margin: 8px 0 10px;
  }

  p { margin-bottom: 3px; }
  .section-heading {
    font-weight: 700; font-style: italic;
    font-size: 13px; color: var(--navy);
    margin: 10px 0 3px;
  }
  .section-heading--lead { margin-top: 0; }
  .sub-heading {
    font-weight: 700; font-style: italic;
    font-size: 12px; color: var(--navy);
    margin: 7px 0 3px;
  }
  .list { list-style: none; }
  .risk {
    display: grid; grid-template-columns: 150px 1fr;
    margin-bottom: 5px;
  }
  .risk__detail p { margin-bottom: 0; }
  .risk__options { padding-left: 12px; }
  .closing { margin-top: 10px; }

  .copyright {
    position: absolute; left: 28px; bottom: 20px;
    font-size: 11px; color: var(--muted);
  }
</style>
</head>
<body>
<main class="spread">

  <article class="page page--front">
    <svg class="wave wave--top" viewBox="0 0 560 70" preserveAspectRatio="none" aria-hidden="true">
      <defs>
        <linearGradient id="topFadeA" x1="0" y1="0" x2="1" y2="0">
          <stop offset="0" stop-color="#3fd8f5"/>
          <stop offset="0.55" stop-color="#5fb0ff"/>
          <stop offset="1" stop-color="#e6f8fd"/>
        </linearGradient>
      </defs>
      <path d="M0 0 H560 V40 C430 12 300 14 160 40 C100 50 40 56 0 58 Z" fill="#e6f8fd"/>
      <path d="M0 0 H470 C400 14 300 20 200 34 C120 44 50 48 0 46 Z" fill="url(#topFadeA)"/>
    </svg>

    <div class="page__body">
      <header class="masthead">
        <h1 class="title">Ankle block:</h1>
        <div class="clinic-name"><span class="clinic-name__mark"></span>the ashbury clinic</div>
      </header>
      <p class="author">Patient information from Dr Tobias Wendell</p>

      <p>You are scheduled to have surgery on your foot. It is my normal practice to offer and perform (with your consent) an ankle block. This is an optional injection of numbing liquid to the nerves which supply your foot. The ankle block can be performed when you are awake, sedated or under general anaesthesia.</p>
      <p>The ankle block can be combined with a general anaesthetic and with sedation. It can also be used to allow surgery to be performed with you wide awake in certain cases.</p>
      <p>Having or not having an ankle block does not change the pre-operative fasting guidelines you have been given. There is a fee for performing an ankle block. Please consult my initial introductory email and terms of business for details.</p>

      <h2 class="section-heading">What are the benefits:</h2>
      <ul class="list">
        <li>1 - Excellent pain relief - usually 10 - 14 hours (and rarely 24 - 48 hours)</li>
        <li>2 - Avoiding traditional painkillers, resulting in less post-operative nausea and vomiting</li>
        <li>3 - The option to avoid a general anaesthetic (if you wish)</li>
        <li>4 - A faster recovery from the general anaesthetic</li>
        <li>5 - Certain surgery requires an overnight stay in hospital without an ankle block</li>
      </ul>

      <h2 class="section-heading">What are the risks?</h2>
      <p>As with all injections, there is the risk of bruising, bleeding and infection.</p>
      <div class="risk">
        <span>1 - Nerve damage -</span>
        <div class="risk__detail">
          <p>Occurs in 1 in 5000 nerve blocks.</p>
          <p>Creates an area of numbness or weakness/paralysis in some or all of the foot.</p>
          <p>The majority of nerve injuries will heal themselves within a year.</p>
          <p>There is no treatment to fix it.</p>
          <p>If the block has not worn off after 72 hours, please let me know.</p>
        </div>
      </div>
      <div class="risk">
        <span>2 - Failure -</span>
        <div class="risk__detail">
          <p>The success rate with ankle blocks is 98 - 99%.</p>
          <p>Some blocks will fail, partially or totally.</p>
          <p>If the block fails totally, I will discuss repeating it with your consent.</p>
        </div>
      </div>
      <div class="risk">
        <span>3 - Pain during operation -</span>
        <div class="risk__detail">
          <p>If you choose to have wide awake surgery or surgery under sedation, the surgery will stop and I will discuss three options with you:</p>
          <div class="risk__options">
            <p>- more numbing liquid to be injected by the surgeon</p>
            <p>- more sedation / painkiller</p>
            <p>- having a general anaesthetic</p>
          </div>
        </div>
      </div>

      <p class="closing">If you decide to undergo surgery awake or sedated, there is a risk you will need to have a general anaesthetic if you feel pain. This is why the fasting instructions for awake surgery and general anaesthesia are the same.</p>
    </div>

    <svg class="wave wave--bottom" viewBox="0 0 560 62" preserveAspectRatio="none" aria-hidden="true">
      <defs>
        <linearGradient id="bottomFadeA" x1="0" y1="0" x2="1" y2="0">
          <stop offset="0" stop-color="#5fb0ff"/>
          <stop offset="1" stop-color="#3fd8f5"/>
        </linearGradient>
      </defs>
      <path d="M240 62 C290 20 400 6 560 18 V62 Z" fill="#e6f8fd"/>
      <path d="M300 62 C340 36 440 26 560 36 V62 Z" fill="url(#bottomFadeA)"/>
    </svg>
    <p class="copyright">© Dr Tobias Wendell. All rights reserved.</p>
  </article>

  <article class="page page--back">
    <svg class="wave wave--top" viewBox="0 0 560 70" preserveAspectRatio="none" aria-hidden="true">
      <defs>
        <linearGradient id="topFadeB" x1="0" y1="0" x2="1" y2="0">
          <stop offset="0" stop-color="#3fd8f5"/>
          <stop offset="0.55" stop-color="#5fb0ff"/>
          <stop offset="1" stop-color="#e6f8fd"/>
        </linearGradient>
      </defs>
      <path d="M0 0 H560 V36 C430 10 300 12 160 34 C100 44 40 50 0 50 Z" fill="#e6f8fd"/>
      <path d="M0 0 H470 C400 12 300 18 200 30 C120 40 50 42 0 40 Z" fill="url(#topFadeB)"/>
    </svg>

    <div class="page__body">
      <h2 class="section-heading section-heading--lead">How is it done</h2>
      <h3 class="sub-heading">If you choose awake surgery or surgery with sedation</h3>
      <ul class="list">
        <li>Numbing liquid is injected around the nerves which supply your foot.</li>
        <li>The ankle block takes 5 - 10 minutes to perform and requires 4 - 5 injections.</li>
        <li>It takes approximately 10 - 20 minutes to make your foot numb to pain.</li>
        <li>I will check the ankle block is working before we start surgery using cold spray.</li>
        <li>Sensations of touch, pressure, vibration and movement will still be felt.</li>
        <li>I will use a screen so you can't see the surgery (unless you would like to see).</li>
        <li>Some patients bring headphones to block out the noise of the operation.</li>
      </ul>
      <p>The ankle block can be combined with a general anaesthetic and with sedation. It can also be used to allow surgery to be performed with you wide awake in certain cases. Having or not having an ankle block does not change the pre-operative fasting guidelines you have been given. There is a fee for performing an ankle block. Please consult my initial introductory email and terms of business for details.</p>

      <h3 class="sub-heading">If you choose a general anaesthetic -</h3>
      <ul class="list">
        <li>I will perform the ankle block after I start the general anaesthetic.</li>
        <li>You should wake up from your surgery with a comfortable and numb foot/feet.</li>
        <li>If you wake in pain, we can repeat the ankle block or provide traditional painkillers.</li>
        <li>Whatever you choose, there will be a cannula placed in your hand and heart and oxygen monitoring throughout.</li>
      </ul>

      <h2 class="section-heading">After surgery:</h2>
      <p>You will go to the recovery area and then onto the ward when you are ready. It will be difficult to walk while the block is working, so physiotherapists will help you first walk. If you need crutches they will teach you how to use them.</p>
      <p>Your foot will be numb and so you will not feel where your foot is in relation to nearby objects. As a result, it is easy to knock your foot. Please take extra care while your foot is still numb.</p>
      <p>As the block wears off, the foot may feel slightly painful, tingly or hot. At this point you should take the painkillers I have prescribed. Depending on your medical history you will have up to three painkillers. I would suggest you start with all three. You will also have an anti-sickness medicine prescribed in case one of the painkillers (typically codeine or morphine) makes you feel sick.</p>
      <p>Occasionally (1 - 2%) pain when the block wears off will be severe. In this case contact your surgeon's secretary. We can use stronger pain medication, but there will be a charge for writing and getting the private prescription to you via courier (please see my terms of business).</p>

      <h2 class="section-heading">The alternative</h2>
      <p>If you do not have an ankle block your surgery can still proceed. Post-operative pain can be managed with traditional painkillers. However, you are more likely to need an overnight stay or feel sick after the anaesthetic.</p>
      <p>If you have any further questions about an ankle block, I will see you on the day of your surgery. Alternatively, you can request the following optional services (as mentioned in my terms of business).</p>
    </div>

    <svg class="wave wave--bottom" viewBox="0 0 560 62" preserveAspectRatio="none" aria-hidden="true">
      <defs>
        <linearGradient id="bottomFadeB" x1="0" y1="0" x2="1" y2="0">
          <stop offset="0" stop-color="#5fb0ff"/>
          <stop offset="1" stop-color="#3fd8f5"/>
        </linearGradient>
      </defs>
      <path d="M240 62 C290 20 400 6 560 18 V62 Z" fill="#e6f8fd"/>
      <path d="M300 62 C340 36 440 26 560 36 V62 Z" fill="url(#bottomFadeB)"/>
    </svg>
    <p class="copyright">© Dr Tobias Wendell. All rights reserved.</p>
  </article>

</main>
</body>
</html>
```